Business Card

I need a business card that really pops for a potential customer or person who refers a personal injury lead. I want to highlight our office locations, but only address that needs to be on the card is my office's main address. I want a sleek, modern and minimalist design.

```html
<!DOCTYPE html>
<html lang="en">
<head>
<meta charset="utf-8">
<title>Harlow Injury Lawyers – Business Card</title>
<link rel="stylesheet" href="https://fonts.googleapis.com/css2?family=Montserrat:wght@400;500;700&display=swap">
<style>
  :root {
    --backdrop: #1c1c1c;
    --card: #050505;
    --ink: #ffffff;
    --ink-soft: #e6e6e6;
    --rule: #d9d9d9;
  }
  * { margin: 0; padding: 0; box-sizing: border-box; }
  html, body {
    width: 1200px; height: 1108px; overflow: hidden;
    background: var(--backdrop);
    font-family: "Montserrat", sans-serif;
    color: var(--ink);
  }
  .card {
    position: absolute;
    width: 700px; height: 400px;
    background: var(--card);
  }
  .card--front { left: 60px; top: 90px; }
  .card--back { left: 440px; top: 620px; }

  .firm-name {
    position: absolute;
    font-weight: 500;
    letter-spacing: 0;
    line-height: 1.2;
    color: var(--ink);
    white-space: nowrap;
  }
  .card--front .firm-name {
    left: 50%; top: 50%;
    transform: translate(-50%, -50%);
    font-size: 40px;
  }
  .card--back .firm-name {
    left: 60px; top: 188px;
    font-size: 20px;
  }

  .divider {
    position: absolute; left: 330px; top: 110px;
    width: 1px; height: 180px; background: var(--rule);
  }
  .contact { position: absolute; left: 360px; top: 112px; }
  .contact__name { font-size: 22px; font-weight: 700; line-height: 1.1; }
  .contact__role { font-size: 13px; font-weight: 400; color: var(--ink-soft); margin-top: 3px; }
  .contact__list { list-style: none; margin-top: 22px; }
  .contact__item {
    display: flex; align-items: center; gap: 10px;
    font-size: 13px; color: var(--ink-soft); line-height: 1.55;
  }
  .contact__item svg { width: 11px; height: 11px; flex: none; fill: var(--ink); }
  .contact__address {
    margin-top: 18px; margin-left: 21px;
    font-size: 13px; color: var(--ink-soft); line-height: 1.4; font-style: normal;
  }
</style>
</head>
<body>
  <section class="card card--front" aria-label="Business card front">
    <p class="firm-name">Harlow Injury Lawyers</p>
  </section>

  <section class="card card--back" aria-label="Business card back">
    <p class="firm-name">Harlow Injury Lawyers</p>
    <div class="divider"></div>
    <div class="contact">
      <p class="contact__name">Dean Callister</p>
      <p class="contact__role">CEO &amp; Founder</p>
      <ul class="contact__list">
        <li class="contact__item">
          <svg viewBox="0 0 12 12" aria-hidden="true"><path d="M2.5 1h2l1 3-1.5 1a7 7 0 0 0 3 3l1-1.5 3 1v2A1.5 1.5 0 0 1 9.5 11 8.5 8.5 0 0 1 1 2.5 1.5 1.5 0 0 1 2.5 1z"/></svg>
          555 210-4476
        </li>
        <li class="contact__item">
          <svg viewBox="0 0 12 12" aria-hidden="true"><path d="M1 3h10v6.5H1z M1 3l5 3.5L11 3" stroke="#050505" stroke-width="0.8"/></svg>
          info@harlowlaw.com
        </li>
        <li class="contact__item">
          <svg viewBox="0 0 12 12" aria-hidden="true"><circle cx="6" cy="6" r="5"/><path d="M1 6h10M6 1c2 2 2 8 0 10M6 1c-2 2-2 8 0 10" stroke="#050505" stroke-width="0.8" fill="none"/></svg>
          www.harlowlaw.com
        </li>
      </ul>
      <address class="contact__address">418 Larkin Ave, #112<br>Brookdale, OH 43190</address>
    </div>
  </section>
</body>
</html>
```